Amber Ridge Publishing Web Page Design

Design a website for my new start up publishing company - Amber Ridge Publishing, the first work published by ARP with be a new book by M.R. Theodor called Silent Ledger. The prototype for the book cover is attached.

Target Market(s)

Worldwide, all readers of mystery, fiction, etc.

Industry/Entity Type

Book Publisher

Coding

Coded - Design and coding required

Number of Pages Required

1 page

```html
<!DOCTYPE html>
<html lang="en">
<head>
<meta charset="utf-8">
<title>Amber Ridge Publishing</title>
<link href="https://fonts.googleapis.com/css2?family=Poppins:wght@200;300;400;500;700;800&family=Arimo:wght@400;500&display=swap" rel="stylesheet">
<style>
:root{
  --ink:#1a1a1a;
  --text:#2b2b2b;
  --muted:#6e6e6e;
  --light-num:#c4c4c4;
  --band:#6f7680;
  --band-sky:#8fa3b8;
  --panel:#fafafa;
  --footer:#f0f0f0;
  --copy-bar:#b9b9b9;
  --button:#d3d3d3;
  --button-dark:#6a6a6a;
  --rule:#d8d8d8;
  --white:#ffffff;
  --cover-deep:#1b2060;
  --cover-mid:#3a4aa0;
}
*{margin:0;padding:0;box-sizing:border-box}
html,body{width:1200px;height:3031px;overflow:hidden;background:var(--white)}
body{position:relative;font-family:"Arimo",Arial,sans-serif;color:var(--text)}
.abs{position:absolute}

/* header */
.brand{left:47px;top:18px;font-family:"Arimo",Arial,sans-serif;font-size:17px;letter-spacing:.3px;color:var(--ink)}
.nav{top:21px;right:78px;display:flex;gap:40px;font-size:11.5px;color:var(--ink)}

/* hero */
.hero-author{left:0;width:724px;top:186px;text-align:center;font-family:"Poppins",sans-serif;font-size:12px;letter-spacing:3px;color:var(--ink)}
.hero-title{left:0;width:724px;top:212px;text-align:center;font-family:"Poppins",sans-serif;font-weight:800;font-size:57px;letter-spacing:-.5px;color:var(--ink)}
.hero-desc{left:0;width:724px;top:303px;text-align:center;font-size:11px;color:var(--ink)}
.hero-link{left:0;width:724px;top:356px;text-align:center;font-size:12px;color:var(--ink)}
.hero-book{left:770px;top:72px;width:360px;height:480px}

/* choice band */
.band{left:0;top:564px;width:1200px;height:259px;background:linear-gradient(180deg,var(--band) 0%,#7d8794 60%,var(--band) 100%)}
.band-heading{left:0;width:1200px;top:655px;text-align:center;font-family:"Poppins",sans-serif;font-weight:300;font-size:28px;color:var(--white)}
.card{top:745px;width:262px;height:149px;background:var(--white);border-radius:4px;box-shadow:0 14px 22px rgba(0,0,0,.14);text-align:center}
.card-num{margin-top:30px;font-family:"Poppins",sans-serif;font-weight:300;font-size:46px;color:var(--light-num);line-height:1.2}
.card-label{margin-top:3px;font-size:11px;color:var(--ink)}

/* about */
.about-photo{left:0;top:999px;width:480px;height:429px}
.about-panel{left:480px;top:999px;width:720px;height:429px;background:var(--panel)}
.about-heading{left:527px;top:1046px;font-size:22px;color:var(--ink)}
.about-copy{left:527px;top:1144px;width:440px;font-size:12px;line-height:39px;color:var(--ink)}

/* recommended */
.rec-rule{left:39px;top:1503px;width:1122px;height:1px;background:var(--rule)}
.rec-heading{left:0;width:1200px;top:1488px;text-align:center}
.rec-heading span{background:var(--white);padding:0 12px;font-family:"Poppins",sans-serif;font-weight:300;font-size:22px;color:var(--ink)}
.rec-book{left:45px;top:1567px;width:180px;height:235px}
.rec-title{left:39px;top:1813px;font-family:"Poppins",sans-serif;font-weight:300;font-size:13px;color:var(--muted)}
.rec-link{left:45px;top:1837px;font-size:8px;color:var(--muted);border-bottom:1px solid #c77;padding-bottom:1px}
.btn-view{left:60px;top:1887px;width:144px;height:37px;background:var(--button);box-shadow:0 3px 5px rgba(0,0,0,.25);font-size:10px;color:var(--ink);display:flex;align-items:center;justify-content:center}

/* quote */
.quote{left:150px;width:900px;top:2026px;text-align:center;font-family:"Poppins",sans-serif;font-weight:200;font-size:28px;line-height:32px;color:var(--ink)}
.quote-by{left:0;width:1200px;top:2122px;text-align:center;font-family:"Poppins",sans-serif;font-size:15px;color:var(--ink)}

/* contact */
.contact-heading{left:460px;width:400px;top:2253px;text-align:center;font-family:"Poppins",sans-serif;font-weight:700;font-size:27px;color:var(--ink)}
.field{border-bottom:1px solid var(--rule);font-size:12px;color:var(--muted);padding-bottom:6px}
.btn-send{left:125px;top:2576px;width:83px;height:36px;background:var(--button-dark);box-shadow:0 3px 5px rgba(0,0,0,.3);font-size:10px;color:var(--white);display:flex;align-items:center;justify-content:center}

/* footer */
.footer{left:0;top:2654px;width:1200px;height:335px;background:var(--footer)}
.foot-link{top:2756px;width:190px;text-align:center;font-size:13px;color:var(--ink)}
.foot-rule{left:210px;top:2786px;width:780px;height:1px;background:#e2e2e2}
.foot-copy{left:230px;width:740px;top:2830px;text-align:center;font-size:11px;line-height:21px;color:var(--ink)}
.social{top:2942px;left:0;width:1200px;display:flex;justify-content:center;gap:22px;font-size:11px;color:var(--ink)}
.social span{display:flex;align-items:center;gap:5px}
.social i{display:inline-block;width:8px;height:8px;border-radius:50%;background:var(--ink)}
.copy-bar{left:0;top:2989px;width:1200px;height:42px;background:var(--copy-bar);font-size:11px;color:var(--ink);display:flex;align-items:center;justify-content:center}
</style>
</head>
<body>

<header>
  <div class="abs brand">AMBER RIDGE PUBLISHING</div>
  <nav class="abs nav"><span>HOME</span><span>ABOUT</span><span>CONTACT</span></nav>
</header>

<section class="hero">
  <div class="abs hero-author">AUTHOR: M.R. THEODOR</div>
  <h1 class="abs hero-title">SILENT LEDGER</h1>
  <p class="abs hero-desc">A murder mystery set in the large projects and skyscraper sectors of the construction industry.</p>
  <div class="abs hero-link">READ REVIEW</div>
  <svg class="abs hero-book" viewBox="0 0 360 480" role="img" aria-label="Book cover of Silent Ledger, standing at an angle">
    <defs><linearGradient id="coverA" x1="0" y1="0" x2="1" y2="1"><stop offset="0" stop-color="#101540"/><stop offset=".5" stop-color="var(--cover-mid)"/><stop offset="1" stop-color="var(--cover-deep)"/></linearGradient></defs>
    <ellipse cx="200" cy="440" rx="70" ry="20" fill="#000" opacity=".12"/>
    <polygon points="130,0 350,120 200,470 0,315" fill="url(#coverA)"/>
    <polygon points="350,120 360,130 212,478 200,470" fill="#e6e6e6"/>
  </svg>
</section>

<section class="choice">
  <div class="abs band" role="img" aria-label="Photo of cheerful young people jumping under a cloudy sky, dimmed"></div>
  <h2 class="abs band-heading">What makes us the best choice</h2>
  <div class="abs card" style="left:39px"><div class="card-num">100%</div><div class="card-label">Hardwork</div></div>
  <div class="abs card" style="left:325px"><div class="card-num">100%</div><div class="card-label">Dedication</div></div>
  <div class="abs card" style="left:612px"><div class="card-num">100%</div><div class="card-label">Quality</div></div>
  <div class="abs card" style="left:898px"><div class="card-num">100%</div><div class="card-label">Friendliness</div></div>
</section>

<section class="about">
  <div class="abs about-photo" role="img" aria-label="Photo of a stack of books beside an open laptop" style="background:linear-gradient(110deg,#b89a6a 0%,#6f8aa0 30%,#9a9a9a 55%,#e2e2e2 100%)"></div>
  <div class="abs about-panel"></div>
  <h2 class="abs about-heading">ABOUT US:</h2>
  <p class="abs about-copy">ARP is a new start up and the first author / book it will launch is Silent Ledger which will be published this fall. More authors / books are planned later but for now it is small and fill use the first book to build on.</p>
</section>

<section class="recommended">
  <div class="abs rec-rule"></div>
  <h2 class="abs rec-heading"><span>HIGHLY RECOMMENDED BOOKS</span></h2>
  <svg class="abs rec-book" viewBox="0 0 180 235" role="img" aria-label="Book cover of Silent Ledger thumbnail">
    <defs><linearGradient id="coverB" x1="0" y1="0" x2="1" y2="1"><stop offset="0" stop-color="#101540"/><stop offset=".5" stop-color="var(--cover-mid)"/><stop offset="1" stop-color="var(--cover-deep)"/></linearGradient></defs>
    <ellipse cx="110" cy="215" rx="38" ry="11" fill="#000" opacity=".12"/>
    <polygon points="62,0 172,60 100,228 0,153" fill="url(#coverB)"/>
    <polygon points="172,60 178,65 106,232 100,228" fill="#e6e6e6"/>
  </svg>
  <div class="abs rec-title">Silent Ledger</div>
  <div class="abs rec-link">READ REVIEWS</div>
  <div class="abs btn-view">VIEW ALL BOOKS</div>
</section>

<section class="testimonial">
  <blockquote class="abs quote">"It takes great courage to write great books. Find your courage and find your voice."</blockquote>
  <div class="abs quote-by">Helena Marsh</div>
</section>

<section class="contact">
  <h2 class="abs contact-heading">Contact us</h2>
  <div class="abs field" style="left:120px;top:2359px;width:390px">Your name</div>
  <div class="abs field" style="left:533px;top:2359px;width:390px">Your email</div>
  <div class="abs field" style="left:120px;top:2414px;width:803px">Subject</div>
  <div class="abs field" style="left:120px;top:2469px;width:803px;height:84px">Your message</div>
  <div class="abs btn-send">SEND</div>
</section>

<footer>
  <div class="abs footer"></div>
  <div class="abs foot-link" style="left:219px">ABOUT US</div>
  <div class="abs foot-link" style="left:410px">CONTACT</div>
  <div class="abs foot-link" style="left:600px">RECCOMENDATIONS</div>
  <div class="abs foot-link" style="left:791px">BENEFITS</div>
  <div class="abs foot-rule"></div>
  <p class="abs foot-copy">Sed ut perspiciatis unde omnis iste natus error sit voluptatem accusantium doloremque laudantium, totam rem aperiam, eaque ipsa quae ab illo inventore veritatis et quasi architecto beatae vitae dicta sunt explicabo. Nemo enim ipsam voluptatem quia voluptas sit aspernatur aut odit aut fugit, sed quia consequuntur.</p>
  <div class="abs social"><span><i></i>Pagenet</span><span><i></i>Chirpline</span><span><i></i>Searchly</span><span><i></i>Snapframe</span><span><i></i>Pinboardly</span></div>
  <div class="abs copy-bar">© 2018 Copyright:</div>
</footer>

</body>
</html>
```